2 page PSD web design

I need a fairly simple website design built in PSD format for a site / blog in the finance niche. My current web address is www.spreadledgerhub.com. Yield Ledger Hub is a site that teaches people how to trade options with a focus on income strategies.

I need a simple homepage built and then another similar template for all other pages including blog posts.

The rough design layout is shown attached excel file. It is similar to www.marcusfelbring.com although I don't like the colors on his site at all. My logo is attached also, so the colours should be aligned with my logo.

In the header section, I will be giving away a free ebook called "Fluff-Free Manual for Calendar Wings" so I will need a 2D and 3D book cover designed as well. The design should be aligned with my logo and site design.

Industry/Entity Type

Finance

Requirements
Must have
• Everything is detailed in the excel file, but here is a list of must have items:

My current logo
ebook design and sign up section
under the ebook sign up section, need a big bold heading - "HELPING YOU TRADE IRON CONDORS AND OTHER INCOME STRATEGIES WITHOUT THE BS"
6 sidebar sections as detailed in excel file
Social Proof at top right, on the same line / level as the logo
"home advertise contact" in the top left in small discreet font
Should not have
• Do not want any photos or images on either of the pages

```html
<!DOCTYPE html>
<html lang="en">
<head>
<meta charset="utf-8">
<title>Yield Ledger Hub</title>
<link href="https://fonts.googleapis.com/css2?family=Arimo:wght@400;700&display=swap" rel="stylesheet">
<style>
:root{
  --blue:#1f7fc4;
  --blue-dark:#1565a8;
  --blue-light:#4fa6e0;
  --ink:#333;
  --grey:#666;
  --soft:#999;
  --panel:#f4f4f4;
  --line:#d6d6d6;
  --thumb:#ececec;
  --bar:#1b1b1b;
  --footer:#5e5e5e;
  --white:#fff;
}
*{box-sizing:border-box;margin:0;padding:0}
html,body{width:731px;height:1200px;overflow:hidden}
body{position:relative;background:#f2f2f2;font-family:"Arimo",Arial,sans-serif;color:var(--ink)}
.abs{position:absolute}

.top-bar{left:0;top:0;width:731px;height:20px;background:linear-gradient(#2a2a2a,#0d0d0d)}
.top-links{left:92px;top:6px;font-size:7px;color:var(--white)}
.top-links span{margin:0 4px}

.masthead{left:0;top:20px;width:731px;height:80px;background:linear-gradient(#f6f6f6,#e6e6e6)}
.brand{left:100px;top:46px;display:flex;align-items:center;gap:10px}
.brand-dot{width:46px;height:46px;border-radius:50%;background:var(--blue)}
.brand-name{font-size:22px;color:var(--blue);font-weight:400}
.social-proof{left:418px;top:47px;font-size:10px;color:#111}
.social{top:62px;width:19px;height:19px;border-radius:2px}

.nav{left:0;top:100px;width:731px;height:25px;background:linear-gradient(var(--blue-light),var(--blue-dark));display:flex;padding-left:92px}
.nav a{font-size:7px;color:var(--white);text-decoration:none;line-height:25px;text-align:center;border-right:1px solid rgba(255,255,255,.35)}

.optin{left:91px;top:132px;width:549px;height:140px;background:linear-gradient(#fff,#f0f0f0);box-shadow:0 8px 10px -6px rgba(0,0,0,.25)}
.optin-ask{left:12px;top:14px;font-size:8px;color:var(--grey)}
.optin-lead{left:12px;top:36px;font-size:12px;font-weight:700;color:var(--blue);line-height:14px}
.optin-free{left:12px;top:64px;font-size:24px;font-weight:700;color:var(--blue)}
.optin-copy{left:14px;top:101px;width:230px;font-size:8px;line-height:13px;color:var(--grey)}
.ebook{left:247px;top:6px;width:104px;height:128px;border-radius:3px;background:linear-gradient(90deg,#555 0,#999 12%,#2a8ad6 14%,#1b6fb8 100%)}
.optin-hint{left:381px;top:11px;font-size:8px;color:var(--grey)}
.field{left:382px;width:157px;height:23px;background:var(--white);border:1px solid #e2e2e2;font-size:8px;color:#aaa;padding:7px 8px}
.cta{left:386px;top:94px;width:152px;height:28px;border-radius:3px;background:linear-gradient(var(--blue-light),var(--blue-dark));color:var(--white);font-size:13px;text-align:center;line-height:28px}

.tagline{left:0;top:293px;width:727px;text-align:center;font-size:20px;font-weight:700;color:var(--grey);line-height:22px}

.section-label{left:91px;width:355px;font-size:7px;color:var(--grey);border-bottom:1px solid #bbb;padding-bottom:3px}
.post{left:91px;width:355px;height:120px}
.post h2{font-size:18px;font-weight:400;color:#444;position:absolute;left:0;top:0}
.post .thumb{position:absolute;left:2px;top:26px;width:84px;height:77px;background:var(--thumb)}
.post .meta{position:absolute;left:91px;top:28px;font-size:5.5px;color:#444}
.post .bubble{position:absolute;left:328px;top:25px;width:17px;height:11px;border:1px solid #bbb;border-radius:2px;background:#f6f6f6;font-size:5px;text-align:center;line-height:9px}
.post p{position:absolute;left:91px;width:262px;font-size:7px;line-height:9.5px;color:#444}
.post .more{position:absolute;left:94px;top:109px;width:92px;height:14px;border-radius:7px;background:var(--blue);color:var(--white);font-size:6.5px;text-align:center;line-height:14px}

.side{left:464px;width:175px}
.work{top:354px;height:128px;background:linear-gradient(#fff,#e6e6e6);border:1px solid var(--line);text-align:center}
.work h3{font-size:20px;font-weight:700;color:#222;margin-top:9px;line-height:23px}
.work .sub{font-size:20px;font-weight:700;color:var(--grey);line-height:23px}
.work p{font-size:8px;line-height:10px;margin:12px 20px 0}
.work .go{font-size:16px;font-weight:700;color:var(--blue);margin-top:15px}
.beginners{top:487px;height:127px;overflow:hidden;background:linear-gradient(#f2f2f2,#c8c8c8)}
.beginners h3{position:absolute;top:16px;width:100%;text-align:center;font-size:13px;font-weight:700;color:#333}
.beginners p{position:absolute;top:63px;width:100%;text-align:center;font-size:13px;font-weight:700;color:var(--white);line-height:17px}
.panel-head{height:20px;background:linear-gradient(var(--blue-light),var(--blue-dark));color:var(--white);font-size:13px;font-weight:700;padding-left:10px;line-height:20px}
.training-item{height:30px;margin-top:2px;background:linear-gradient(#fff,#e4e4e4);border:1px solid #ddd;display:flex;align-items:center;gap:12px;padding-left:7px;font-size:10px;font-weight:700;color:#555}
.sponsors{top:790px;height:135px;background:var(--white);border:1px solid var(--line)}
.sponsor-grid{display:grid;grid-template-columns:80px 80px;gap:4px;padding:6px 5px}
.sponsor-grid div{height:48px;border:1px solid #ddd}
.ad{top:930px;height:135px;background:linear-gradient(#8cc3ea,#2a85cc 40%,#1f76bd);text-align:center;font-size:18px;color:rgba(255,255,255,.25);padding-top:54px}
.newsletter{top:1072px;height:62px;background:#3a3a3a;padding:6px 6px}
.newsletter p{font-size:7px;color:var(--white);line-height:9px}
.newsletter .email{position:absolute;left:6px;top:38px;width:94px;height:18px;background:var(--white);font-size:7px;color:#888;padding:5px 5px}
.newsletter .join{position:absolute;left:104px;top:38px;width:66px;height:18px;background:var(--blue);color:var(--white);font-size:7px;font-weight:700;text-align:center;line-height:18px}

.footer{left:0;top:1146px;width:731px;height:54px;background:var(--footer);color:var(--white);text-align:center}
.footer p{font-size:5.5px;line-height:7px;width:520px;margin:10px auto 0}
.footer small{display:block;font-size:5.5px;margin-top:11px}
</style>
</head>
<body>

<div class="abs top-bar"></div>
<div class="abs top-links">Home<span>|</span>Advertise<span>|</span>Contact</div>

<header class="abs masthead"></header>
<div class="abs brand"><span class="brand-dot"></span><span class="brand-name">Yield Ledger Hub</span></div>
<div class="abs social-proof">JOIN A COMMUNITY OF 4279 AWESOME READERS</div>
<div class="abs social" style="left:543px;background:#3b5998"></div>
<div class="abs social" style="left:568px;background:#4ab3e3"></div>
<div class="abs social" style="left:594px;background:#c4302b"></div>
<div class="abs social" style="left:620px;background:#d9412f"></div>

<nav class="abs nav">
  <a style="width:74px">Articles and Videos</a>
  <a style="width:92px">Trading Philosophy</a>
  <a style="width:82px">Learning Centre</a>
  <a style="width:63px">Free Tools</a>
  <a style="width:78px">Members Only</a>
  <a style="width:71px">Work With Us</a>
  <a style="width:51px">About</a>
</nav>

<section class="abs optin">
  <div class="abs optin-ask">Do You Want To Know The Truth About Iron Condors?</div>
  <div class="abs optin-lead">Learn How To Trade This Amazing<br>Option Income Strategy With My</div>
  <div class="abs optin-free">FREE Ebook</div>
  <div class="abs optin-copy">I will share with you my blueprint and all my tips and tricks for generating consistent monthly income with iron condors</div>
  <div class="abs ebook" role="img" aria-label="Cover of the free ebook Fluff-Free Manual for Calendar Wings"></div>
  <div class="abs optin-hint">Enter your details now for instant access...</div>
  <div class="abs field" style="top:29px">Enter your first name</div>
  <div class="abs field" style="top:61px">Enter your email address</div>
  <div class="abs cta">Get Instant Access!</div>
</section>

<h1 class="abs tagline">HELPING YOU TRADE IRON CONDORS AND OTHER<br>INCOME STRATEGIES WITHOUT THE BS</h1>

<div class="abs section-label" style="top:362px">Latest Posts</div>

<article class="abs post" style="top:381px">
  <h2>Post Heading</h2><div class="thumb"></div>
  <div class="meta">Posted by Dorian Keswick</div><div class="bubble">0</div>
  <p style="top:44px">Lorem ipsum dolor sirt amet consecutor. Lorem ipsum dolor sirt amet consecutor. Lorem ipsum dolor sirt amet consecutor. Lorem ipsum dolor sirt amet consecutor.</p>
  <p style="top:82px;width:220px">Lorem ipsum dolor sirt amet consecutor. Lorem ipsum dolor sirt amet consecutor.</p>
  <div class="more">Click here to Read More</div>
</article>
<article class="abs post" style="top:524px">
  <h2>Post Heading</h2><div class="thumb"></div>
  <div class="meta">Posted by Dorian Keswick</div><div class="bubble">0</div>
  <p style="top:44px">Lorem ipsum dolor sirt amet consecutor. Lorem ipsum dolor sirt amet consecutor. Lorem ipsum dolor sirt amet consecutor. Lorem ipsum dolor sirt amet consecutor.</p>
  <p style="top:82px;width:220px">Lorem ipsum dolor sirt amet consecutor. Lorem ipsum dolor sirt amet consecutor.</p>
  <div class="more">Click here to Read More</div>
</article>
<article class="abs post" style="top:662px">
  <h2>Post Heading</h2><div class="thumb"></div>
  <div class="meta">Posted by Dorian Keswick</div><div class="bubble">0</div>
  <p style="top:44px">Lorem ipsum dolor sirt amet consecutor. Lorem ipsum dolor sirt amet consecutor. Lorem ipsum dolor sirt amet consecutor. Lorem ipsum dolor sirt amet consecutor.</p>
  <p style="top:82px;width:220px">Lorem ipsum dolor sirt amet consecutor. Lorem ipsum dolor sirt amet consecutor.</p>
  <div class="more">Click here to Read More</div>
</article>

<div class="abs section-label" style="top:815px">Featured Posts</div>

<article class="abs post" style="top:834px">
  <h2>Post Heading</h2><div class="thumb"></div>
  <div class="meta">Posted by Dorian Keswick</div><div class="bubble">0</div>
  <p style="top:44px">Lorem ipsum dolor sirt amet consecutor. Lorem ipsum dolor sirt amet consecutor. Lorem ipsum dolor sirt amet consecutor. Lorem ipsum dolor sirt amet consecutor.</p>
  <p style="top:82px;width:220px">Lorem ipsum dolor sirt amet consecutor. Lorem ipsum dolor sirt amet consecutor.</p>
  <div class="more">Click here to Read More</div>
</article>
<article class="abs post" style="top:972px">
  <h2>Post Heading</h2><div class="thumb"></div>
  <div class="meta">Posted by Dorian Keswick</div><div class="bubble">0</div>
  <p style="top:44px">Lorem ipsum dolor sirt amet consecutor. Lorem ipsum dolor sirt amet consecutor. Lorem ipsum dolor sirt amet consecutor. Lorem ipsum dolor sirt amet consecutor.</p>
  <p style="top:82px;width:220px">Lorem ipsum dolor sirt amet consecutor. Lorem ipsum dolor sirt amet consecutor.</p>
  <div class="more">Click here to Read More</div>
</article>

<aside>
  <div class="abs side work">
    <h3>WORK WITH US</h3>
    <div class="sub">ONE-ONE-ONE</div>
    <p>We're ready to help you achievethe success you're looking for</p>
    <div class="go">CLICK HERE</div>
  </div>

  <div class="abs side beginners">
    <svg class="abs" style="left:0;top:0" width="175" height="127" viewBox="0 0 175 127">
      <defs><linearGradient id="arcBlue" x1="0" y1="0" x2="0" y2="1"><stop offset="0" stop-color="#5aaee6"/><stop offset="1" stop-color="#1a6fb6"/></linearGradient></defs>
      <path d="M0 62 Q87 20 175 62 L175 127 L0 127 Z" fill="#fff"/>
      <path d="M0 66 Q87 26 175 66 L175 127 L0 127 Z" fill="url(#arcBlue)"/>
    </svg>
    <h3>NEW TO OPTIONS?</h3>
    <p>Check out our<br>comprehensive<br>training program</p>
  </div>

  <div class="abs side" style="top:620px">
    <div class="panel-head">Free Training</div>
    <div style="height:14px;background:#fff;border:1px solid #ddd;border-top:0"></div>
    <div class="training-item"><svg width="22" height="18" viewBox="0 0 22 18"><path d="M1 3h7l2 2h11v12H1z" fill="#e9b949" stroke="#b8862a"/><rect x="4" y="1" width="12" height="9" fill="#3d8fd0"/><path d="M1 8h20l-2 9H1z" fill="#f4cf6a" stroke="#b8862a"/></svg>Volatility Tutorials</div>
    <div class="training-item"><svg width="22" height="18" viewBox="0 0 22 18"><path d="M1 3h7l2 2h11v12H1z" fill="#e9b949" stroke="#b8862a"/><rect x="4" y="1" width="12" height="9" fill="#3d8fd0"/><path d="M1 8h20l-2 9H1z" fill="#f4cf6a" stroke="#b8862a"/></svg>Iron Condor Tutorials</div>
    <div class="training-item"><svg width="22" height="18" viewBox="0 0 22 18"><path d="M1 3h7l2 2h11v12H1z" fill="#e9b949" stroke="#b8862a"/><rect x="4" y="1" width="12" height="9" fill="#3d8fd0"/><path d="M1 8h20l-2 9H1z" fill="#f4cf6a" stroke="#b8862a"/></svg>Income Trading Tutorials</div>
    <div class="training-item"><svg width="22" height="18" viewBox="0 0 22 18"><path d="M1 3h7l2 2h11v12H1z" fill="#e9b949" stroke="#b8862a"/><rect x="4" y="1" width="12" height="9" fill="#3d8fd0"/><path d="M1 8h20l-2 9H1z" fill="#f4cf6a" stroke="#b8862a"/></svg>Free Tools and Resources</div>
  </div>

  <div class="abs side sponsors">
    <div class="panel-head">Top Sponsors</div>
    <div class="sponsor-grid"><div></div><div></div><div></div><div></div></div>
  </div>

  <div class="abs side ad">Advertisement</div>

  <div class="abs side newsletter">
    <p>Stay up to date with Yield Ledger Hub. New articles and tutorials delivered straight to your inbox</p>
    <div class="email">ENTER YOUR EMAIL</div>
    <div class="join">Let's Do This</div>
  </div>
</aside>

<footer class="abs footer">
  <p>Disclaimer: This site and any products and courses offered by Yield Ledger Hub are for general informational and educational purposes only. Investing, including that in vehicles originating in the share market, carries with it a degree of risk which must be appropriately managed. Visitors to this website are strongly advised not only to educate themselves appropriately prior to investing in any share market product, but also discuss thesuitability of such products to their overall wealth objectives with a licensed financial professional.</p>
  <small>Copyright © Yield Ledger Hub</small>
</footer>

</body>
</html>
```